Search Fund needs a PowerPoint template design

We need a eye-catching and compelling PowerPoint design for a new company based in Chicago called Harrow Ridge Partners. We are search fund with a primary mission to acquire a founder/family/entrepreneur owned businesses (This is similar to a Private Equity firm). Our goal is to offer investors a unique avenue to invest in an attractive business acquisition while providing business owners with an alternative path to exit. We would like the design to reflect crisp and professional nature that many financial firms present. The template should build on the design of the logo including expanding a logical color palette. The presentation will be used to describe facts regarding the firm, financial data and key messaging that we want our investors and potential partners to takeaway.

Target Market(s)

Financial Investors

Industry/Entity Type

Finance

Font styles to use
Serif
Sans Serif

Colors

Designer to choose colors to be used in the design.

Requirements
Must have
• Should include cover page and slide examples. Attractive data displays (graphs, charts, infographics etc.); Compelling cover; fly pages to put in between sections; table of contents page. Needs to have white space to add text.
Should not have
• Do not redesign the logo or change the logo colors. Additional colors should be added to the PowerPoint template

```html
<!DOCTYPE html>
<html lang="en">
<head>
<meta charset="utf-8">
<title>Harrow Ridge Partners – Presentation Template</title>
<link rel="stylesheet" href="https://fonts.googleapis.com/css2?family=Lato:wght@300;400;700;900&family=Exo+2:wght@600&display=swap">
<style>
  :root{
    --canvas:#cbcbcb;
    --blue:#1372c4;
    --blue-light:#3a9be0;
    --blue-pale:#9cc6ee;
    --ink:#231f20;
    --charcoal:#3d3d3d;
    --slate:#5a5a5a;
    --grey:#9a9a9a;
    --grey-light:#d8d8d8;
    --teal:#3a9ba5;
    --deep-teal:#1f4d5b;
    --white:#ffffff;
    --muted:#555555;
  }
  *{margin:0;padding:0;box-sizing:border-box}
  html,body{width:1200px;height:1200px;overflow:hidden;background:var(--canvas)}
  .board{position:relative;width:1200px;height:1200px;font-family:"Lato",sans-serif}
  .slide{position:absolute;display:block;box-shadow:0 1px 3px rgba(0,0,0,.18)}
  .slide--hero{left:385px;top:52px;width:430px;height:302px}
  .col-1{left:139px}.col-2{left:450px}.col-3{left:760px}
  .row-1{top:440px}.row-2{top:679px}.row-3{top:918px}
  .slide--grid{width:304px;height:228px}
  .icon-defs{position:absolute;width:0;height:0}

  .fill-white{fill:var(--white)}
  .fill-blue{fill:var(--blue)}
  .fill-ink{fill:var(--ink)}
  .fill-charcoal{fill:var(--charcoal)}
  .fill-slate{fill:var(--slate)}
  .fill-grey{fill:var(--grey)}
  .fill-grey-light{fill:var(--grey-light)}
  .fill-teal{fill:var(--teal)}
  .fill-deep-teal{fill:var(--deep-teal)}

  text{font-family:"Lato",sans-serif}
  .brand{font-weight:900;letter-spacing:.04em}
  .brand--blue{fill:var(--blue)}
  .brand--white{fill:var(--white)}
  .tagline{font-family:"Exo 2",sans-serif;font-weight:600;fill:var(--white);text-anchor:middle}
  .hdr{font-size:5px;letter-spacing:.06em}
  .hdr-muted{fill:#b0b0b0;font-weight:400}
  .hdr-strong{font-weight:900}
  .hdr-strong--blue{fill:var(--blue)}
  .hdr-strong--ink{fill:var(--ink)}
  .hdr-strong--white{fill:var(--white)}
  .footer-url{font-size:3.4px;fill:var(--white);font-weight:700}
  .footer-url--muted{fill:var(--muted)}
  .page-no{font-size:6px;fill:var(--white)}
  .page-no--ink{fill:var(--ink)}
  .tiny{font-size:2.9px;fill:var(--muted);text-anchor:middle}
  .tiny--white{fill:var(--white)}
  .tiny-title{font-size:3px;fill:var(--blue);font-weight:700;text-anchor:middle}
  .year{font-size:6px;fill:var(--muted);text-anchor:middle}
  .body-copy{font-size:4.6px;fill:#333;text-anchor:middle}
  .pct{font-weight:300;text-anchor:middle}
  .cycle-label{font-size:11px;font-weight:300;fill:#333;text-anchor:middle}
  .cycle-num{font-size:13px;font-weight:300;fill:var(--white);text-anchor:middle}
  .option-title{font-size:4.8px;fill:var(--blue)}
  .option-copy{font-size:4.4px;fill:var(--white);text-anchor:middle}
  .connector{fill:none;stroke:var(--blue);stroke-width:1}
  .icon-stroke{fill:none;stroke:var(--white);stroke-width:1.6;stroke-linejoin:round;stroke-linecap:round}
</style>
</head>
<body>
<main class="board">

  <svg class="icon-defs" aria-hidden="true">
    <defs>
      <symbol id="icon-plane" viewBox="0 0 24 24"><path class="icon-stroke" d="M3 11 L21 4 L15 20 L11 13 Z M11 13 L21 4"/></symbol>
      <symbol id="icon-gear" viewBox="0 0 24 24"><circle class="icon-stroke" cx="12" cy="12" r="3"/><circle class="icon-stroke" cx="12" cy="12" r="6.5"/><circle cx="12" cy="12" r="8" fill="none" stroke="#fff" stroke-width="2.4" stroke-dasharray="2.6 3.7"/></symbol>
      <symbol id="icon-pin" viewBox="0 0 24 24"><path class="icon-stroke" d="M12 21 C7 15 6 12 6 9.5 A6 6 0 0 1 18 9.5 C18 12 17 15 12 21 Z"/><circle class="icon-stroke" cx="12" cy="9.5" r="2"/></symbol>
      <symbol id="icon-diamond" viewBox="0 0 24 24"><path class="icon-stroke" d="M6 4 H18 L22 9 L12 21 L2 9 Z M2 9 H22 M9 4 L12 9 L15 4 M12 9 V21"/></symbol>
      <symbol id="icon-monitor" viewBox="0 0 24 24"><rect class="icon-stroke" x="3" y="4" width="18" height="12" rx="1"/><path class="icon-stroke" d="M12 16 V20 M8 20 H16"/></symbol>
      <linearGradient id="photo-tone" x1="0" y1="0" x2="0" y2="1">
        <stop offset="0" stop-color="#626d77"/>
        <stop offset=".55" stop-color="#3c434a"/>
        <stop offset="1" stop-color="#262a2f"/>
      </linearGradient>
      <linearGradient id="device-tone" x1="0" y1="0" x2="0" y2="1">
        <stop offset="0" stop-color="#1c2a3a"/>
        <stop offset="1" stop-color="#15202c"/>
      </linearGradient>
    </defs>
  </svg>

  <!-- Cover, large -->
  <svg class="slide slide--hero" viewBox="0 0 538 378">
    <rect role="img" aria-label="Photo of a laptop on a desk showing financial charts" width="538" height="378" fill="url(#photo-tone)"/>
    <polygon class="fill-grey-light" points="0,0 538,0 538,14 0,86"/>
    <polygon class="fill-blue" points="395,34 538,14 538,66"/>
    <text class="brand brand--blue" x="14" y="38" font-size="20">HARROW RIDGE PARTNERS</text>
    <text class="tagline" x="268" y="190" font-size="18">Lorem ipsum dolor sit amet etuer</text>
    <text class="tagline" x="268" y="214" font-size="18">met etuer this lorem ipatm.</text>
    <polygon class="fill-grey-light" points="0,315 538,337 538,341 0,319"/>
    <polygon class="fill-blue" points="0,319 538,341 538,378 0,378"/>
    <text class="footer-url" x="20" y="361" font-size="5.5">www.harrowridgepartners.com</text>
    <text class="page-no" x="508" y="366" font-size="9">1.</text>
  </svg>

  <!-- 1 Cover -->
  <svg class="slide slide--grid col-1 row-1" viewBox="0 0 380 285">
    <rect role="img" aria-label="Photo of a laptop on a desk showing financial charts" width="380" height="285" fill="url(#photo-tone)"/>
    <polygon class="fill-grey-light" points="0,0 380,0 380,10 0,62"/>
    <polygon class="fill-blue" points="280,24 380,10 380,48"/>
    <text class="brand brand--blue" x="9" y="28" font-size="14">HARROW RIDGE PARTNERS</text>
    <text class="tagline" x="190" y="142" font-size="12.5">Lorem ipsum dolor sit amet etuer</text>
    <text class="tagline" x="190" y="160" font-size="12.5">met etuer this lorem ipatm.</text>
    <polygon class="fill-grey-light" points="0,238 380,254 380,257 0,241"/>
    <polygon class="fill-blue" points="0,241 380,257 380,285 0,285"/>
    <text class="footer-url" x="14" y="272">www.harrowridgepartners.com</text>
    <text class="page-no" x="358" y="276">1.</text>
  </svg>

  <!-- 2 Title -->
  <svg class="slide slide--grid col-2 row-1" viewBox="0 0 380 285">
    <rect class="fill-white" width="380" height="285"/>
    <polygon class="fill-blue" points="0,0 380,0 380,195 160,170 0,145"/>
    <polygon class="fill-grey" points="0,145 160,170 0,192"/>
    <text class="brand brand--white" x="190" y="60" font-size="14" text-anchor="middle">HARROW RIDGE PARTNERS</text>
    <text x="190" y="88" font-size="5" fill="#9cc6ee" text-anchor="middle">LOREM IPSUM</text>
    <text x="190" y="111" font-size="12" font-weight="900" fill="#fff" text-anchor="middle" letter-spacing=".05em">LOREM IPSUM DOLOR</text>
    <rect class="fill-blue" x="175" y="200" width="30" height="0.8" opacity=".6"/>
    <text class="body-copy" y="218"><tspan x="190">Lorem ipsum dolor sit amet, consectetur adipiscing elit. Morbi id erat</tspan><tspan x="190" dy="6">vitae eros lacinia auctor. Donec ut porttitor eros. Cras facilisis pharetra</tspan><tspan x="190" dy="6">nulla, vel dictum nisi facilisis a. Morbi dapibus metus vitae scelerisque</tspan><tspan x="190" dy="6">euismod. Morbi volutpat risus eu elit placerat, eu porttitor sapien</tspan><tspan x="190" dy="6">placerat. Mauris imperdiet sagittis tortor vel tempus.</tspan></text>
    <text class="footer-url footer-url--muted" x="190" y="275" text-anchor="middle">www.harrowridgepartners.com</text>
    <text class="page-no page-no--ink" x="352" y="276">2.</text>
  </svg>

  <!-- 3 Timeline -->
  <svg class="slide slide--grid col-3 row-1" viewBox="0 0 380 285">
    <rect class="fill-white" width="380" height="285"/>
    <text class="hdr" x="19" y="20"><tspan class="hdr-muted">TITLE</tspan><tspan class="hdr-muted" dx="6">|</tspan><tspan class="hdr-strong hdr-strong--blue" dx="6">TEXT HEADLINE</tspan></text>
    <g>
      <circle class="fill-blue" cx="75" cy="100" r="19"/><use href="#icon-plane" x="65" y="90" width="20" height="20"/>
      <circle class="fill-grey" cx="189" cy="100" r="19"/><use href="#icon-pin" x="179" y="90" width="20" height="20"/>
      <circle class="fill-blue" cx="305" cy="100" r="19"/><use href="#icon-diamond" x="295" y="90" width="20" height="20"/>
      <circle class="fill-blue" cx="132" cy="180" r="19"/><use href="#icon-gear" x="122" y="170" width="20" height="20"/>
      <circle class="fill-grey" cx="247" cy="180" r="19"/><use href="#icon-monitor" x="237" y="170" width="20" height="20"/>
    </g>
    <g>
      <rect class="fill-grey" x="48" y="138" width="55" height="4"/>
      <rect class="fill-blue" x="106" y="138" width="55" height="4"/>
      <rect class="fill-grey" x="164" y="138" width="55" height="4"/>
      <rect class="fill-blue" x="222" y="138" width="55" height="4"/>
      <rect class="fill-grey" x="280" y="138" width="55" height="4"/>
      <polygon class="fill-grey" points="72,142 78,142 75,146"/>
      <polygon class="fill-blue" points="130,138 136,138 133,134"/>
      <polygon class="fill-grey" points="188,142 194,142 191,146"/>
      <polygon class="fill-blue" points="245,138 251,138 248,134"/>
      <polygon class="fill-grey" points="303,142 309,142 306,146"/>
    </g>
    <text class="year" x="133" y="74">2016</text>
    <text class="tiny-title" x="133" y="85">LOREM IPSUM</text>
    <text class="tiny" y="91"><tspan x="133">Donec auctor varius</tspan><tspan x="133" dy="4">dui, vel commodo</tspan><tspan x="133" dy="4">lectus bibendum.</tspan></text>
    <text class="year" x="248" y="74">2018</text>
    <text class="tiny-title" x="248" y="85">LOREM IPSUM</text>
    <text class="tiny" y="91"><tspan x="248">Donec auctor varius</tspan><tspan x="248" dy="4">dui, vel commodo</tspan><tspan x="248" dy="4">lectus bibendum.</tspan></text>
    <text class="year" x="76" y="170">2015</text>
    <text class="tiny-title" x="76" y="181">LOREM IPSUM</text>
    <text class="tiny" y="187"><tspan x="76">Donec auctor varius</tspan><tspan x="76" dy="4">dui, vel commodo</tspan><tspan x="76" dy="4">lectus bibendum.</tspan></text>
    <text class="year" x="190" y="170">2017</text>
    <text class="tiny-title" x="190" y="181">LOREM IPSUM</text>
    <text class="tiny" y="187"><tspan x="190">Donec auctor varius</tspan><tspan x="190" dy="4">dui, vel commodo</tspan><tspan x="190" dy="4">lectus bibendum.</tspan></text>
    <text class="year" x="305" y="170">2019</text>
    <text class="tiny-title" x="305" y="181">LOREM IPSUM</text>
    <text class="tiny" y="187"><tspan x="305">Donec auctor varius</tspan><tspan x="305" dy="4">dui, vel commodo</tspan><tspan x="305" dy="4">lectus bibendum.</tspan></text>
    <polygon class="fill-charcoal" points="240,258 380,250 380,268"/>
    <polygon class="fill-blue" points="0,240 380,268 380,285 0,285"/>
    <text class="footer-url" x="14" y="277">www.harrowridgepartners.com</text>
    <text class="page-no" x="358" y="278">3.</text>
  </svg>

  <!-- 4 Cycle -->
  <svg class="slide slide--grid col-1 row-2" viewBox="0 0 380 285">
    <rect class="fill-white" width="380" height="285"/>
    <g stroke="#fff" stroke-width="3">
      <path class="fill-blue" d="M96.8 104.7 A98 98 0 0 1 190 37 L190 89 A46 46 0 0 0 146.3 120.8 Z"/>
      <path class="fill-ink" d="M190 37 A98 98 0 0 1 283.2 104.7 L233.7 120.8 A46 46 0 0 0 190 89 Z"/>
      <path class="fill-grey" d="M283.2 104.7 A98 98 0 0 1 247.6 214.3 L217 172.2 A46 46 0 0 0 233.7 120.8 Z"/>
      <path class="fill-blue" d="M247.6 214.3 A98 98 0 0 1 132.4 214.3 L163 172.2 A46 46 0 0 0 217 172.2 Z"/>
      <path class="fill-ink" d="M132.4 214.3 A98 98 0 0 1 96.8 104.7 L146.3 120.8 A46 46 0 0 0 163 172.2 Z"/>
    </g>
    <text class="cycle-label" x="190" y="123">THE</text>
    <text class="cycle-label" x="190" y="137">CYCLE</text>
    <text class="tiny" y="146"><tspan x="190">Lorem ipsum eget molestie</tspan><tspan x="190" dy="4">nunc aliquam elementum</tspan><tspan x="190" dy="4">lectus et tristique.</tspan></text>
    <text class="cycle-num" x="159" y="72">01.</text>
    <text class="cycle-num" x="234" y="79">02.</text>
    <text class="cycle-num" x="253" y="171">03.</text>
    <text class="cycle-num" x="174" y="206">04.</text>
    <text class="cycle-num" x="117" y="149">05.</text>
    <text class="tiny tiny--white" y="80"><tspan x="159">Maecenas eget molestie</tspan><tspan x="159" dy="4">nunc. Aliquam elementum,</tspan><tspan x="159" dy="4">lectus et tristique.</tspan></text>
    <text class="tiny tiny--white" y="87"><tspan x="236">Maecenas eget</tspan><tspan x="236" dy="4">nunc. Aliquam</tspan><tspan x="236" dy="4">elementum.</tspan></text>
    <text class="tiny tiny--white" y="179"><tspan x="253">Maecenas eget</tspan><tspan x="253" dy="4">nunc. Aliquam</tspan><tspan x="253" dy="4">elementum.</tspan></text>
    <text class="tiny tiny--white" y="214"><tspan x="174">Maecenas eget molestie</tspan><tspan x="174" dy="4">nunc. Aliquam elementum.</tspan></text>
    <text class="tiny tiny--white" y="157"><tspan x="117">Maecenas eget</tspan><tspan x="117" dy="4">molestie nunc.</tspan><tspan x="117" dy="4">Aliquam lectus.</tspan></text>
    <polygon class="fill-charcoal" points="240,258 380,250 380,268"/>
    <polygon class="fill-blue" points="0,240 380,268 380,285 0,285"/>
    <text class="footer-url" x="14" y="277">www.harrowridgepartners.com</text>
    <text class="page-no" x="358" y="278">4.</text>
  </svg>

  <!-- 5 Device infographic -->
  <svg class="slide slide--grid col-2 row-2" viewBox="0 0 380 285">
    <rect class="fill-ink" width="380" height="285"/>
    <text class="hdr" x="19" y="22"><tspan class="hdr-muted">TITLE</tspan><tspan class="hdr-muted" dx="6">|</tspan><tspan class="hdr-strong hdr-strong--white" dx="6">TEXT HEADLINE</tspan></text>
    <rect role="img" aria-label="Line illustration of a smartphone showing a pie chart" x="142" y="60" width="98" height="178" rx="9" fill="url(#device-tone)"/>
    <path class="connector" d="M142 88 H118 M142 165 H118 M240 88 H264 M240 165 H264"/>
    <text class="option-title" x="56" y="89">TITLE OPTION</text>
    <text class="option-title" x="56" y="166">TITLE OPTION</text>
    <text class="option-title" x="266" y="89">TITLE OPTION</text>
    <text class="option-title" x="266" y="166">TITLE OPTION</text>
    <text class="option-copy" y="100"><tspan x="75">Lorem ipsum dolor sit amet,</tspan><tspan x="75" dy="6">consectetur adipiscing elit.</tspan><tspan x="75" dy="6">Morbi id erat vitae eros</tspan><tspan x="75" dy="6">lacinia auctor.</tspan></text>
    <text class="option-copy" y="177"><tspan x="75">Lorem ipsum dolor sit amet,</tspan><tspan x="75" dy="6">consectetur adipiscing elit.</tspan><tspan x="75" dy="6">Morbi id erat vitae eros</tspan><tspan x="75" dy="6">lacinia auctor.</tspan></text>
    <text class="option-copy" y="100"><tspan x="305">Lorem ipsum dolor sit amet,</tspan><tspan x="305" dy="6">consectetur adipiscing elit.</tspan><tspan x="305" dy="6">Morbi id erat vitae eros</tspan><tspan x="305" dy="6">lacinia auctor.</tspan></text>
    <text class="option-copy" y="177"><tspan x="305">Lorem ipsum dolor sit amet,</tspan><tspan x="305" dy="6">consectetur adipiscing elit.</tspan><tspan x="305" dy="6">Morbi id erat vitae eros</tspan><tspan x="305" dy="6">lacinia auctor.</tspan></text>
    <polygon class="fill-grey" points="0,262 380,236 380,239 0,265"/>
    <polygon class="fill-blue" points="0,265 380,239 380,285 0,285"/>
    <text class="page-no" x="14" y="278">5.</text>
    <text class="footer-url" x="364" y="272" text-anchor="end">www.harrowridgepartners.com</text>
  </svg>

  <!-- 6 Donut -->
  <svg class="slide slide--grid col-3 row-2" viewBox="0 0 380 285">
    <rect class="fill-white" width="380" height="285"/>
    <text class="hdr" x="19" y="22"><tspan class="hdr-muted">TITLE</tspan><tspan class="hdr-muted" dx="6">|</tspan><tspan class="hdr-strong hdr-strong--blue" dx="6">TEXT HEADLINE</tspan></text>
    <g fill="none" stroke-width="14" transform="rotate(-90 190 139)">
      <circle cx="190" cy="139" r="78" stroke="#231f20" stroke-dasharray="88 402" stroke-dashoffset="0"/>
      <circle cx="190" cy="139" r="78" stroke="#1372c4" stroke-dasharray="122.5 367.5" stroke-dashoffset="-88"/>
      <circle cx="190" cy="139" r="78" stroke="#9a9a9a" stroke-dasharray="122.5 367.5" stroke-dashoffset="-210.5"/>
      <circle cx="190" cy="139" r="78" stroke="#1372c4" stroke-dasharray="157 333" stroke-dashoffset="-333"/>
    </g>
    <text x="190" y="132" font-size="17" font-weight="400" fill="#231f20" text-anchor="middle">4 SECTION</text>
    <text class="tiny" y="143"><tspan x="190">Maecenas eget molestie nunc. Aliquam</tspan><tspan x="190" dy="4">elementum, lectus et tristique</tspan><tspan x="190" dy="4">scelerisque, odio augue tempor lectus.</tspan></text>
    <text class="pct" x="50" y="84" font-size="15" fill="#1372c4">28<tspan font-size="9">%</tspan></text>
    <text class="pct" x="310" y="84" font-size="15" fill="#231f20">18<tspan font-size="9">%</tspan></text>
    <text class="pct" x="50" y="196" font-size="15" fill="#9a9a9a">25<tspan font-size="9">%</tspan></text>
    <text class="pct" x="310" y="196" font-size="15" fill="#9a9a9a">25<tspan font-size="9">%</tspan></text>
    <text class="tiny" y="95"><tspan x="50">Maecenas eget molestie</tspan><tspan x="50" dy="4">nunc. Aliquam elementum,</tspan><tspan x="50" dy="4">lectus et tristique.</tspan></text>
    <text class="tiny" y="95"><tspan x="310">Maecenas eget molestie</tspan><tspan x="310" dy="4">nunc. Aliquam elementum,</tspan><tspan x="310" dy="4">lectus et tristique.</tspan></text>
    <text class="tiny" y="207"><tspan x="50">Maecenas eget molestie</tspan><tspan x="50" dy="4">nunc. Aliquam elementum,</tspan><tspan x="50" dy="4">lectus et tristique.</tspan></text>
    <text class="tiny" y="207"><tspan x="310">Maecenas eget molestie</tspan><tspan x="310" dy="4">nunc. Aliquam elementum,</tspan><tspan x="310" dy="4">lectus et tristique.</tspan></text>
    <polygon class="fill-charcoal" points="240,258 380,250 380,268"/>
    <polygon class="fill-blue" points="0,240 380,268 380,285 0,285"/>
    <text class="footer-url" x="14" y="277">www.harrowridgepartners.com</text>
    <text class="page-no" x="358" y="278">6.</text>
  </svg>

  <!-- 7 Peaks -->
  <svg class="slide slide--grid col-1 row-3" viewBox="0 0 380 285">
    <rect class="fill-white" width="380" height="285"/>
    <text class="hdr" x="19" y="22"><tspan class="hdr-muted">TITLE</tspan><tspan class="hdr-muted" dx="6">|</tspan><tspan class="hdr-strong hdr-strong--ink" dx="6">TEXT HEADLINE</tspan></text>
    <polygon class="fill-grey" points="296,138 380,285 210,285"/>
    <polygon class="fill-blue" points="168,108 270,285 65,285"/>
    <polygon class="fill-charcoal" points="63,178 125,285 0,285"/>
    <polygon class="fill-teal" points="240,233 270,285 210,285"/>
    <polygon class="fill-deep-teal" points="95,233 125,285 65,285"/>
    <text class="pct" x="168" y="80" font-size="19" fill="#1372c4">72%</text>
    <text class="pct" x="63" y="160" font-size="16" fill="#231f20">35%</text>
    <text class="pct" x="294" y="125" font-size="16" fill="#9a9a9a">58%</text>
    <g fill="#fff" text-anchor="middle">
      <text x="168" y="194" font-size="6.5">TITLE OPTION</text>
      <text y="209" font-size="4.5"><tspan x="168">Lorem ipsum dolor sit amet,</tspan><tspan x="168" dy="6">consectetur adipiscing elit.</tspan><tspan x="168" dy="6">Morbi id erat vitae eros</tspan><tspan x="168" dy="6">lacinia auctor.</tspan></text>
      <text x="295" y="210" font-size="6.5">TITLE OPTION</text>
      <text y="222" font-size="4.5"><tspan x="295">Lorem ipsum dolor sit amet,</tspan><tspan x="295" dy="6">consectetur adipiscing elit.</tspan><tspan x="295" dy="6">Morbi id erat vitae eros</tspan><tspan x="295" dy="6">lacinia auctor.</tspan></text>
      <text y="227" font-size="6.5"><tspan x="63">TITLE</tspan><tspan x="63" dy="8">OPTION</tspan></text>
      <text y="249" font-size="4.5"><tspan x="63">Lorem ipsum dolor sit</tspan><tspan x="63" dy="6">amet, consectetur</tspan><tspan x="63" dy="6">adipiscing elit.</tspan></text>
    </g>
  </svg>

  <!-- 8 Icon grid -->
  <svg class="slide slide--grid col-2 row-3" viewBox="0 0 380 285">
    <rect class="fill-white" width="380" height="285"/>
    <text class="hdr" x="19" y="22"><tspan class="hdr-muted">TITLE</tspan><tspan class="hdr-muted" dx="6">|</tspan><tspan class="hdr-strong hdr-strong--ink" dx="6">TEXT HEADLINE</tspan></text>
    <g>
      <circle class="fill-blue" cx="70" cy="75" r="17"/><use href="#icon-plane" x="61" y="66" width="18" height="18"/>
      <circle class="fill-grey" cx="149" cy="75" r="17"/><use href="#icon-gear" x="140" y="66" width="18" height="18"/>
      <circle class="fill-blue" cx="228" cy="75" r="17"/><use href="#icon-pin" x="219" y="66" width="18" height="18"/>
      <circle class="fill-grey" cx="307" cy="75" r="17"/><use href="#icon-diamond" x="298" y="66" width="18" height="18"/>
      <circle class="fill-grey" cx="70" cy="168" r="17"/><use href="#icon-plane" x="61" y="159" width="18" height="18"/>
      <circle class="fill-blue" cx="149" cy="168" r="17"/><use href="#icon-gear" x="140" y="159" width="18" height="18"/>
      <circle class="fill-grey" cx="228" cy="168" r="17"/><use href="#icon-pin" x="219" y="159" width="18" height="18"/>
      <circle class="fill-blue" cx="307" cy="168" r="17"/><use href="#icon-diamond" x="298" y="159" width="18" height="18"/>
    </g>
    <g>
      <text class="tiny-title" x="70" y="106">LOREM IPSUM</text><text class="tiny" y="112"><tspan x="70">Donec auctor varius dui, vel</tspan><tspan x="70" dy="4">commodo lectus bibendum in.</tspan><tspan x="70" dy="4">Vivamus ut lacus.</tspan></text>
      <text class="tiny-title" x="149" y="106">LOREM IPSUM</text><text class="tiny" y="112"><tspan x="149">Donec auctor varius dui, vel</tspan><tspan x="149" dy="4">commodo lectus bibendum in.</tspan><tspan x="149" dy="4">Vivamus ut lacus.</tspan></text>
      <text class="tiny-title" x="228" y="106">LOREM IPSUM</text><text class="tiny" y="112"><tspan x="228">Donec auctor varius dui, vel</tspan><tspan x="228" dy="4">commodo lectus bibendum in.</tspan><tspan x="228" dy="4">Vivamus ut lacus.</tspan></text>
      <text class="tiny-title" x="307" y="106">LOREM IPSUM</text><text class="tiny" y="112"><tspan x="307">Donec auctor varius dui, vel</tspan><tspan x="307" dy="4">commodo lectus bibendum in.</tspan><tspan x="307" dy="4">Vivamus ut lacus.</tspan></text>
      <text class="tiny-title" x="70" y="199">LOREM IPSUM</text><text class="tiny" y="205"><tspan x="70">Donec auctor varius dui, vel</tspan><tspan x="70" dy="4">commodo lectus bibendum in.</tspan><tspan x="70" dy="4">Vivamus ut lacus.</tspan></text>
      <text class="tiny-title" x="149" y="199">LOREM IPSUM</text><text class="tiny" y="205"><tspan x="149">Donec auctor varius dui, vel</tspan><tspan x="149" dy="4">commodo lectus bibendum in.</tspan><tspan x="149" dy="4">Vivamus ut lacus.</tspan></text>
      <text class="tiny-title" x="228" y="199">LOREM IPSUM</text><text class="tiny" y="205"><tspan x="228">Donec auctor varius dui, vel</tspan><tspan x="228" dy="4">commodo lectus bibendum in.</tspan><tspan x="228" dy="4">Vivamus ut lacus.</tspan></text>
      <text class="tiny-title" x="307" y="199">LOREM IPSUM</text><text class="tiny" y="205"><tspan x="307">Donec auctor varius dui, vel</tspan><tspan x="307" dy="4">commodo lectus bibendum in.</tspan><tspan x="307" dy="4">Vivamus ut lacus.</tspan></text>
    </g>
    <polygon class="fill-charcoal" points="240,258 380,250 380,268"/>
    <polygon class="fill-blue" points="0,240 380,268 380,285 0,285"/>
    <text class="footer-url" x="14" y="277">www.harrowridgepartners.com</text>
    <text class="page-no" x="358" y="278">8.</text>
  </svg>

  <!-- 9 Closing -->
  <svg class="slide slide--grid col-3 row-3" viewBox="0 0 380 285">
    <rect class="fill-charcoal" width="380" height="285"/>
    <polygon class="fill-slate" points="0,92 240,118 0,140"/>
    <polygon fill="#8a8a8a" points="0,92 240,118 240,120 0,94"/>
    <polygon class="fill-blue" points="0,138 380,93 380,285 0,285"/>
    <text x="190" y="68" font-size="21" font-weight="700" fill="#fff" text-anchor="middle">THANK YOU</text>
    <text class="brand brand--white" x="190" y="168" font-size="14" text-anchor="middle">HARROW RIDGE PARTNERS</text>
    <g fill="#fff" font-size="4.4" text-anchor="middle">
      <text x="190" y="214">Street Name, City Name, Zipcode-12345</text>
      <text x="190" y="233">&#9743; 012-345-6789</text>
      <text x="190" y="245">&#9993; info@harrowridgepartners.com</text>
      <text x="190" y="276">www.harrowridgepartners.com</text>
    </g>
  </svg>

</main>
</body>
</html>
```